Flyer design needed for services offered and to show reviews from previous customers

I would like a Flyer designed showing some of the services i offer:
-LED lighting upgrades (pot lights, accent & commercial)
-Electrical repairs & Service work
- Fayglowen lighting
- TV wall mounts
My website is Voltarisa.ca if you need any photos from there in higher quality please let me know and i can provide them.

I want it to have a couple reviews from previous customers (attached links to facebook and google page)
Google:
https://revpage.example/r/QZ8kd4mtpWhaJXo/review
Facebook:
https://www.socialbook.example/Voltarisa-Contracting-Ltd-552918730461283

```html
<!DOCTYPE html>
<html lang="en">
<head>
<meta charset="utf-8">
<title>Voltarisa Contracting Ltd – Services Flyer</title>
<link rel="stylesheet" href="https://fonts.googleapis.com/css2?family=Red+Hat+Display:wght@500;700;900&family=Roboto:wght@400;500&display=swap">
<style>
  :root {
    --orange: #f58220;
    --orange-dark: #e06d0f;
    --charcoal: #3d3d3d;
    --grey-panel: #4a4a4a;
    --grey-mid: #6b6b6b;
    --card-border: #5a5a5a;
    --ink: #222222;
    --white: #ffffff;
    --backdrop: #ececec;
  }
  * { box-sizing: border-box; margin: 0; padding: 0; }
  html, body { width: 1200px; height: 1200px; overflow: hidden; }
  body {
    background: var(--backdrop);
    font-family: "Roboto", Arial, sans-serif;
    color: var(--ink);
    position: relative;
  }
  .flyer {
    position: absolute;
    left: 190px; top: 22px;
    width: 820px; height: 1155px;
    background: var(--white);
    overflow: hidden;
    box-shadow: 0 6px 24px rgba(0,0,0,.18);
  }
  .flyer-shapes { position: absolute; inset: 0; }
  .hero-photo {
    position: absolute; left: 0; top: 0; width: 820px; height: 300px;
    background: linear-gradient(160deg, #8b8a86 0%, #5a5650 35%, #34302c 70%, #6e6a64 100%);
  }
  .brand-badge {
    position: absolute; left: 560px; top: 50px;
    width: 228px; height: 228px; border-radius: 50%;
    background: var(--white);
    border: 6px solid #e2e2e2;
    display: flex; flex-direction: column; align-items: center; justify-content: center;
    text-align: center;
    font-family: "Red Hat Display", Arial, sans-serif;
    font-weight: 900; color: #111;
    letter-spacing: 2px;
  }
  .brand-badge .brand-name { font-size: 30px; line-height: 1.1; }
  .brand-badge .brand-sub { font-size: 17px; line-height: 1.4; }
  .intro {
    position: absolute; left: 55px; top: 312px; width: 710px;
    color: var(--white); text-align: center;
    font-size: 15.5px; line-height: 20px;
  }
  .section-label {
    position: absolute; left: 240px; top: 484px; width: 340px; height: 60px;
    display: flex; align-items: center; justify-content: center;
    font-family: "Red Hat Display", Arial, sans-serif;
    font-weight: 900; font-size: 48px; color: var(--white);
    letter-spacing: 1px;
  }
  .services { position: absolute; left: 0; top: 585px; width: 820px; }
  .service {
    position: absolute; display: flex; align-items: center; gap: 20px;
    font-family: "Red Hat Display", Arial, sans-serif;
    font-weight: 700; font-size: 21px; color: var(--ink);
  }
  .service small {
    display: block; font-family: "Roboto", Arial, sans-serif;
    font-weight: 400; font-size: 12.5px; line-height: 1; margin-top: 2px;
  }
  .service-icon {
    width: 56px; height: 56px; border-radius: 50%;
    background: var(--orange); flex: none;
    display: flex; align-items: center; justify-content: center;
  }
  .service-led { left: 72px; top: 0; }
  .service-repair { left: 72px; top: 70px; }
  .service-fay { left: 490px; top: 0; }
  .service-tv { left: 490px; top: 70px; }

  .reviews-heading {
    position: absolute; left: 0; top: 740px; width: 820px;
    display: flex; align-items: center; justify-content: center; gap: 22px;
    font-family: "Red Hat Display", Arial, sans-serif;
    font-weight: 900; font-size: 28px; color: var(--grey-mid);
    letter-spacing: 1px;
  }
  .reviews-heading::before, .reviews-heading::after {
    content: ""; width: 245px; height: 3px; background: var(--orange);
  }
  .review-card {
    position: absolute; top: 796px; height: 270px;
    background: var(--white);
    border: 4px solid var(--card-border);
    border-radius: 16px;
    padding: 12px 10px 10px;
    text-align: center;
  }
  .review-card.r1 { left: 41px; width: 228px; }
  .review-card.r2 { left: 281px; width: 227px; }
  .review-card.r3 { left: 521px; width: 256px; }
  .stars { color: var(--orange); font-size: 22px; letter-spacing: 3px; line-height: 1; margin-bottom: 8px; }
  .quote { font-size: 13.5px; line-height: 17px; color: var(--ink); }
  .reviewer {
    margin-top: 8px;
    font-family: "Red Hat Display", Arial, sans-serif;
    font-weight: 700; font-size: 15px; line-height: 18px;
  }
  .contact-bar {
    position: absolute; left: 0; top: 1088px; width: 820px; height: 44px;
    display: flex; align-items: center; justify-content: center;
    color: var(--white);
    font-family: "Red Hat Display", Arial, sans-serif;
    font-weight: 700; font-size: 19px;
  }
  .contact-item { display: flex; align-items: center; gap: 10px; padding: 0 24px; }
  .contact-item + .contact-item { border-left: 2px solid var(--white); }
</style>
</head>
<body>
<main class="flyer">
  <div class="hero-photo" role="img" aria-label="Photo of a renovated kitchen with dark cabinets and recessed LED lighting"></div>

  <svg class="flyer-shapes" width="820" height="1155" viewBox="0 0 820 1155" aria-hidden="true">
    <polygon points="0,272 500,272 540,232 820,232 820,248 548,248 508,288 0,288" fill="#cfcfcf"/>
    <polygon points="0,288 508,288 548,248 820,248 820,500 0,500" fill="var(--grey-panel)"/>
    <polygon points="0,500 200,500 222,458 598,458 620,500 820,500 820,522 0,522" fill="var(--orange)"/>
    <polygon points="0,522 820,522 820,530 0,530" fill="var(--orange-dark)"/>
    <polygon points="252,480 600,480 578,548 226,548" fill="var(--charcoal)"/>
    <rect x="0" y="930" width="820" height="225" fill="var(--orange)"/>
  </svg>

  <div class="brand-badge">
    <span class="brand-name">VOLTARISA</span>
    <span class="brand-sub">CONTRACTING LTD</span>
  </div>

  <p class="intro">Whether you need some new lighting installed or need your entire panel replaced, we are here to help! Our goal is to provide you with the best possible service. This means the work is done correctly the first time, there is no mess left behind when it’s completed, and your satisfaction is guaranteed. We provide service in Residential, Commercial and Industrial Electrical Systems. Feel free to give us a call, text or email and we will gladly get in touch to schedule a service call or free quote!</p>

  <h2 class="section-label">SERVICES</h2>

  <section class="services">
    <div class="service service-led">
      <span class="service-icon">
        <svg width="30" height="30" viewBox="0 0 24 24" fill="none" stroke="#fff" stroke-width="1.8" stroke-linecap="round"><path d="M9 17h6M10 20h4M12 3a6 6 0 0 0-3.5 10.9c.6.5 1 1.2 1 2.1h5c0-.9.4-1.6 1-2.1A6 6 0 0 0 12 3z"/></svg>
      </span>
      <span>LED lighting upgrades<small>(pot lights, accent &amp; commercial)</small></span>
    </div>
    <div class="service service-repair">
      <span class="service-icon">
        <svg width="30" height="30" viewBox="0 0 24 24" fill="none" stroke="#fff" stroke-width="1.8" stroke-linejoin="round"><circle cx="12" cy="12" r="3.2"/><path d="M12 2.5l1.6 2.6 3-.8.8 3 2.6 1.6-1.2 2.9 1.2 2.9-2.6 1.6-.8 3-3-.8L12 21.5l-1.6-2.6-3 .8-.8-3-2.6-1.6 1.2-2.9L4 9.3l2.6-1.6.8-3 3 .8z"/></svg>
      </span>
      <span>Electrical repairs &amp; Service work</span>
    </div>
    <div class="service service-fay">
      <span class="service-icon">
        <svg width="30" height="30" viewBox="0 0 24 24" fill="none" stroke="#fff" stroke-width="1.8" stroke-linejoin="round"><path d="M3 11l9-7 9 7M5 9.5V20h14V9.5"/><path d="M12 11v4M10.5 15h3" stroke-linecap="round"/></svg>
      </span>
      <span>Fayglowen lighting</span>
    </div>
    <div class="service service-tv">
      <span class="service-icon">
        <svg width="30" height="30" viewBox="0 0 24 24" fill="none" stroke="#fff" stroke-width="1.8" stroke-linecap="round"><rect x="5" y="6" width="14" height="10" rx="1"/><path d="M2 4v14M22 4v14M2 8h3M19 8h3M2 14h3M19 14h3"/></svg>
      </span>
      <span>TV wall mounts</span>
    </div>
  </section>

  <h2 class="reviews-heading">REVIEWS</h2>

  <article class="review-card r1">
    <div class="stars">★★★★★</div>
    <p class="quote">“Dale did some shop work for me and did a great job. Hooked up a couple of hoists and compressor in an old shop that had several renovations. He figured it out. Was very professional, punctual and fair. I would recommend him and will use him again.”</p>
    <p class="reviewer">Morris Pelkey</p>
  </article>
  <article class="review-card r2">
    <div class="stars">★★★★★</div>
    <p class="quote">“over all a very positive experience will definitely recommended and wont hesitate to use them again.”</p>
    <p class="reviewer">Lena Ostrova</p>
  </article>
  <article class="review-card r3">
    <div class="stars">★★★★★</div>
    <p class="quote">“We had Dale install the electricalfor our garage. He was professional, on time and coordinated with our garage contractor to make sure everything was done in sequence. When the inspector came, it was a one and done. When we do our basement renovation, we will definitely be calling Dale back.”</p>
    <p class="reviewer">Lena Ostrova</p>
  </article>

  <footer class="contact-bar">
    <span class="contact-item">
      <svg width="18" height="18" viewBox="0 0 24 24" aria-hidden="true"><circle cx="12" cy="12" r="11" fill="#fff"/><path d="M8.5 6.5l2 2-1.2 1.6a8 8 0 0 0 4.6 4.6l1.6-1.2 2 2-1.5 1.8c-4.8-.6-8.7-4.5-9.3-9.3z" fill="var(--orange)"/></svg>
      (555) 214-7730
    </span>
    <span class="contact-item">
      <svg width="20" height="16" viewBox="0 0 24 18" fill="none" stroke="#fff" stroke-width="1.8" aria-hidden="true"><rect x="1" y="1" width="22" height="16" rx="1"/><path d="M1 2l11 8 11-8"/></svg>
      Dale@Voltarisa.ca
    </span>
    <span class="contact-item">
      <svg width="18" height="18" viewBox="0 0 24 24" fill="none" stroke="#fff" stroke-width="1.8" aria-hidden="true"><circle cx="12" cy="12" r="10"/><path d="M2 12h20M12 2c3 3 3 17 0 20M12 2c-3 3-3 17 0 20"/></svg>
      www.voltarisa.ca
    </span>
  </footer>
</main>
</body>
</html>
```